Bold & Clean Brisk Harbor Stationary Design

Our company, Brisk Harbor Capital Partners needs a business card, letterhead, and envelope design that all also the formatting standards for quickleafpress.com.

Envelope:
Safe Zone: 9.375" x 4"
Trim Size: 9.5" x 4.15"
Bleed Size: 11.125" 8.625"

Letterhead:
Safe Zone: 10.875" x 8.375"
Trim Size: 11" x 8.5"
Bleed Size: 11.125" x 8.625"

Our mailing address is:
2870 W Larkhill St
Chicago, IL 60618

Please make sure the return address on the envelope is formatted correctly for mailing and the logo is not too large.

Please submit designs in word and PDF form.

Our current letterhead is attached.

We would also like a business card with our existing logo that will meet standards for formatting through Quickleaf Press (quickleafpress.com).

These standards are:
Safe Zone: 3.375" x 1.875"
Trim Size: 3.5" x 2"
Bleed Size: 3.625" x 2.125"

The business card is going to be for Marco Lindqvist, President/CEO of Brisk Harbor Capital Partners. Please include the Address, Telephone Number, Cell Phone Number, Fax Number, Email, and Website Address on the card, which are as follows:

2870 W Larkhill St
Chicago, IL 60618

Tel: (773) 555-0172
Cell: (630) 555-0138
Fax: (63) 555-0194
Email: mrl@briskharborcap.com
Web: www.briskharborcap.com

Please make sure that we can easily change the name of the staff member and job position title ourselves as we will be having cards for individual employees in the future as well.

The back of the card should also have the Brisk Harbor logo on it with our services listed:

Financial Planning | Tax | Solutions for Small Businesses

Industry/Entity Type

Accounting

Requirements
Must have
• envelope
• letterhead
• business card
• All meeting standards set out above.

```html
<!DOCTYPE html>
<html lang="en">
<head>
<meta charset="utf-8">
<title>Brisk Harbor Capital Partners – Stationery</title>
<link href="https://fonts.googleapis.com/css2?family=Arimo:wght@400;700&family=Exo+2:wght@400;500&display=swap" rel="stylesheet">
<style>
  :root{
    --navy:#1f2d5c;
    --orange:#f15a29;
    --paper:#ffffff;
    --backdrop:#ececec;
    --ink:#333;
    --muted:#555;
  }
  *{box-sizing:border-box;margin:0;padding:0}
  html,body{width:1200px;height:937px;overflow:hidden}
  body{background:radial-gradient(circle at 50% 40%,#f7f7f7,var(--backdrop));font-family:"Arimo",Arial,sans-serif;color:var(--ink);position:relative}
  .sheet{position:absolute;background:var(--paper);box-shadow:0 2px 6px rgba(0,0,0,.18)}
  .brand{display:flex;align-items:center;gap:8px;color:var(--navy);font-family:"Arimo",Arial,sans-serif;font-weight:700;line-height:1.05}
  .brand-dot{flex:none;border-radius:50%;background:var(--orange)}
  .web{font-family:"Exo 2",sans-serif;font-weight:500;letter-spacing:.18em;color:#222}
  .icon-ring{position:absolute;border-radius:50%;background:#fff;border:1.5px solid var(--navy);display:flex;align-items:center;justify-content:center}
  .icon-ring svg{display:block}

  /* Letterhead */
  .letterhead{left:185px;top:66px;width:388px;height:547px}
  .letterhead .band{position:absolute;left:0;top:0;width:28px;height:100%;background:var(--navy)}
  .letterhead .brand{position:absolute;left:36px;top:28px;font-size:15px}
  .letterhead .brand-dot{width:30px;height:30px}
  .letter-body{position:absolute;left:35px;top:143px;width:298px;font-size:5.6px;line-height:1.45;color:var(--ink)}
  .letter-body p{margin-bottom:7px}
  .letter-body .gap{margin-bottom:20px}
  .letter-body strong{font-weight:700}
  .signature{width:22px;height:16px;background:linear-gradient(90deg,#cfcfcf,#8a8a8a);margin:4px 0 6px}
  .letter-contacts{position:absolute;left:0;top:458px;width:200px;font-size:4.8px;line-height:1.4;color:var(--muted)}
  .letter-contacts .row{position:absolute;left:44px}
  .letterhead .icon-ring{left:18px;width:17px;height:17px}

  /* Folder */
  .folder{left:636px;top:40px;width:458px;height:576px}
  .folder .band{position:absolute;left:0;top:0;width:41px;height:100%;background:var(--orange)}
  .folder .brand{position:absolute;left:68px;top:258px;font-size:31px;gap:14px}
  .folder .brand-dot{width:62px;height:62px}
  .folder .icon-ring{left:32px;top:527px;width:18px;height:18px}
  .folder .web{position:absolute;left:61px;top:530px;font-size:11px}

  /* Business cards */
  .card-front{left:45px;top:658px;width:177px;height:102px;overflow:hidden}
  .card-front .panel{position:absolute;left:0;top:0}
  .card-contacts{position:absolute;left:0;top:0;width:68px;color:#fff;font-size:4.4px;line-height:1.35;text-align:right}
  .card-contacts .row{position:absolute;right:0}
  .card-front .icon-ring{width:12px;height:12px;border-width:1px}
  .card-front .brand{position:absolute;left:96px;top:50px;font-size:7px;gap:4px}
  .card-front .brand-dot{width:13px;height:13px}
  .card-person{position:absolute;right:8px;top:81px;text-align:right;color:#222}
  .card-person .name{font-size:6px;letter-spacing:.04em}
  .card-person .title{font-size:5px;color:var(--muted)}
  .card-back{left:45px;top:785px;width:177px;height:100px}
  .card-back .brand{position:absolute;left:36px;top:33px;font-size:8px;gap:5px}
  .card-back .brand-dot{width:18px;height:18px}
  .card-services{position:absolute;left:0;right:0;top:66px;text-align:center;font-size:5px;color:var(--muted);letter-spacing:.03em}

  /* Envelope front */
  .envelope-front{left:265px;top:673px;width:429px;height:207px}
  .envelope-front .band{position:absolute;left:0;top:0;width:25px;height:100%;background:var(--navy)}
  .envelope-front .brand{position:absolute;left:33px;top:30px;font-size:15px}
  .envelope-front .brand-dot{width:30px;height:30px}
  .return-address{position:absolute;left:71px;top:70px;font-size:7px;line-height:1.4;color:var(--ink)}
  .envelope-front .icon-ring{left:15px;top:177px;width:17px;height:17px}
  .envelope-front .web{position:absolute;left:37px;top:180px;font-size:8.5px}

  /* Envelope back */
  .envelope-back{left:737px;top:673px;width:431px;height:207px}
  .envelope-back .flap{position:absolute;left:0;top:0;width:100%;height:71px;background:var(--navy);border-radius:0 0 38px 38px;display:flex;align-items:center;justify-content:center}
  .envelope-back .web{color:#fff;font-size:13px}
</style>
</head>
<body>

<!-- Letterhead -->
<section class="sheet letterhead" aria-label="Letterhead">
  <div class="band"></div>
  <div class="brand"><span class="brand-dot"></span><span>Brisk Harbor<br>Capital Partners</span></div>
  <div class="letter-body">
    <p>July 2, 2012</p>
    <p><strong>Dear Client,</strong><br>ABC Building, def St., Country Name</p>
    <p class="gap">Thank you for choosing our team to guide your financial planning this year. This letter confirms the scope of services we discussed during our recent meeting, including tax preparation, quarterly reviews and ongoing support for your small business. Our advisors will contact you shortly to schedule the first planning session and to gather the documents required for your return. We look forward to working with you.</p>
    <p class="gap">Please review the enclosed summary and let us know if any details need to be updated before we begin.</p>
    <p>Thank you for choosing our team to guide your financial planning this year. This letter confirms the scope of services we discussed during our recent meeting, including tax preparation, quarterly reviews and ongoing support for your small business. Our advisors will contact you shortly to schedule the first planning session and to gather the documents required for your return. We look forward to working with you.</p>
    <p>Best Regards,</p>
    <div class="signature" role="img" aria-label="Handwritten signature"></div>
    <p><strong>Daniel Reyes</strong><br>Director<br><br>ABC Building, def St., Country Name</p>
  </div>
  <div class="letter-contacts">
    <span class="icon-ring" style="top:0">
      <svg width="9" height="9" viewBox="0 0 24 24"><path fill="#1f2d5c" d="M6.6 10.8a15.1 15.1 0 0 0 6.6 6.6l2.2-2.2c.3-.3.7-.4 1-.2 1.1.4 2.3.6 3.6.6.6 0 1 .4 1 1V20c0 .6-.4 1-1 1A17 17 0 0 1 3 4c0-.6.4-1 1-1h3.5c.6 0 1 .4 1 1 0 1.3.2 2.5.6 3.6.1.3 0 .7-.2 1z"/></svg>
    </span>
    <div class="row" style="top:2px">(773) 555-0172<br>(630) 555-0138</div>
    <span class="icon-ring" style="top:26px">
      <svg width="8" height="9" viewBox="0 0 24 24"><path fill="#1f2d5c" d="M12 2a7 7 0 0 0-7 7c0 5.2 7 13 7 13s7-7.8 7-13a7 7 0 0 0-7-7zm0 9.5A2.5 2.5 0 1 1 12 6.5a2.5 2.5 0 0 1 0 5z"/></svg>
    </span>
    <div class="row" style="top:27px">2870 W Larkhill St<br>Chicago, IL 60618</div>
    <span class="icon-ring" style="top:52px">
      <svg width="9" height="9" viewBox="0 0 24 24" fill="none" stroke="#1f2d5c" stroke-width="2"><circle cx="12" cy="12" r="9"/><path d="M3 12h18M12 3c3 3 3 15 0 18M12 3c-3 3-3 15 0 18"/></svg>
    </span>
    <div class="row" style="top:54px">mrl@briskharborcap.com<br>www.briskharborcap.com</div>
  </div>
</section>

<!-- Presentation folder -->
<section class="sheet folder" aria-label="Presentation folder">
  <div class="band"></div>
  <div class="brand"><span class="brand-dot"></span><span>Brisk Harbor<br>Capital Partners</span></div>
  <span class="icon-ring">
    <svg width="10" height="10" viewBox="0 0 24 24" fill="none" stroke="#1f2d5c" stroke-width="2"><circle cx="12" cy="12" r="9"/><path d="M3 12h18M12 3c3 3 3 15 0 18M12 3c-3 3-3 15 0 18"/></svg>
  </span>
  <div class="web">www.briskharborcap.com</div>
</section>

<!-- Business card front -->
<section class="sheet card-front" aria-label="Business card front">
  <svg class="panel" width="177" height="102" viewBox="0 0 177 102">
    <path fill="#1f2d5c" d="M0 0H74c8 8 8 20 0 30 8 9 8 21 0 31 8 10 8 22 0 31v10H0z"/>
  </svg>
  <div class="card-contacts">
    <div class="row" style="top:7px">Tel: (773) 555-0172<br>Cell: (630) 555-0138<br>Fax: (63) 555-0194</div>
    <div class="row" style="top:40px">2870 W Larkhill St<br>Chicago, IL 60618</div>
    <div class="row" style="top:72px">mrl@briskharborcap.com<br>www.briskharborcap.com</div>
  </div>
  <span class="icon-ring" style="left:69px;top:10px">
    <svg width="6" height="6" viewBox="0 0 24 24"><path fill="#1f2d5c" d="M6.6 10.8a15.1 15.1 0 0 0 6.6 6.6l2.2-2.2c.3-.3.7-.4 1-.2 1.1.4 2.3.6 3.6.6.6 0 1 .4 1 1V20c0 .6-.4 1-1 1A17 17 0 0 1 3 4c0-.6.4-1 1-1h3.5c.6 0 1 .4 1 1 0 1.3.2 2.5.6 3.6.1.3 0 .7-.2 1z"/></svg>
  </span>
  <span class="icon-ring" style="left:69px;top:40px">
    <svg width="6" height="6" viewBox="0 0 24 24"><path fill="#1f2d5c" d="M12 2a7 7 0 0 0-7 7c0 5.2 7 13 7 13s7-7.8 7-13a7 7 0 0 0-7-7zm0 9.5A2.5 2.5 0 1 1 12 6.5a2.5 2.5 0 0 1 0 5z"/></svg>
  </span>
  <span class="icon-ring" style="left:69px;top:72px">
    <svg width="6" height="6" viewBox="0 0 24 24" fill="none" stroke="#1f2d5c" stroke-width="2"><circle cx="12" cy="12" r="9"/><path d="M3 12h18M12 3c3 3 3 15 0 18M12 3c-3 3-3 15 0 18"/></svg>
  </span>
  <div class="brand"><span class="brand-dot"></span><span>Brisk Harbor<br>Capital Partners</span></div>
  <div class="card-person">
    <div class="name">MARCO LINDQVIST</div>
    <div class="title">President/CEO</div>
  </div>
</section>

<!-- Business card back -->
<section class="sheet card-back" aria-label="Business card back">
  <div class="brand"><span class="brand-dot"></span><span>Brisk Harbor<br>Capital Partners</span></div>
  <div class="card-services">Financial Planning | Tax | Solutions for Small Businesses</div>
</section>

<!-- Envelope front -->
<section class="sheet envelope-front" aria-label="Envelope front">
  <div class="band"></div>
  <div class="brand"><span class="brand-dot"></span><span>Brisk Harbor<br>Capital Partners</span></div>
  <address class="return-address" style="font-style:normal">2870 W Larkhill St<br>Chicago, IL 60618</address>
  <span class="icon-ring">
    <svg width="9" height="9" viewBox="0 0 24 24" fill="none" stroke="#1f2d5c" stroke-width="2"><circle cx="12" cy="12" r="9"/><path d="M3 12h18M12 3c3 3 3 15 0 18M12 3c-3 3-3 15 0 18"/></svg>
  </span>
  <div class="web">www.briskharborcap.com</div>
</section>

<!-- Envelope back -->
<section class="sheet envelope-back" aria-label="Envelope back">
  <div class="flap"><span class="web">www.briskharborcap.com</span></div>
</section>

</body>
</html>
```